Wordpress Design Project

Moraby Pathways is a social entrepreneurship program that organizes and leads development projects in and educational expeditions to Guatemala in order to promote economic development.

We want our website to convey our sustainable business model with colors (greens, yellows, organges,like our logo, etc.) that match our logo, which will be integrated throughout the site, as well as our slogan (Wander, Gather, Reach higher, Come along the Journey).

We want the entire site to appear simple and easy to navigate. We want our name and logo to be featured prominently at the top of our home page as well as our slogan with very large (revolving/changing) photographs featured below or as a background to the page. If possible we would like quotes, testimonials about our programs, or statistics on Guatemala to be printed over these photos.

The first of the sections headings displayed should be eXplore (About Moraby) and underneath will appear our Mission and Philosophy, History, Advisory Board, and Founder information. The second should be eXperience with Our Approach, Our Partners here and abroad, Themed Trips, Pricing and Sample Trips, and the $5 Quest. The third should be eXpect More (Benefits) with Online Store and Past Trips below. The remaining section header should be Request a Proposal.

Target Market(s)

U.S. and Canadian university students and professors and philanthropic or social entrepreneurship organizations

Requirements
Must have
• - include a space for the video on the homepage
- logo, company name and slogan, and large colorful photographs as listed in the description
Nice to have
• http://www.brightloomfund.org/
http://tallcedarproject.org/
Should not have
• -not crowded or overwhelmed with text or visuals

```html
<!DOCTYPE html>
<html lang="en">
<head>
<meta charset="utf-8">
<title>Moraby Pathways</title>
<link href="https://fonts.googleapis.com/css2?family=Open+Sans:wght@400;600;700&family=Ubuntu:wght@500;700&display=swap" rel="stylesheet">
<style>
:root{
  --green:#2f8a2a;
  --green-dark:#236b1f;
  --green-head:#2e7d2c;
  --lime:#b7cd1c;
  --brown:#4a2716;
  --brown-dark:#361a0e;
  --text:#4d4d4d;
  --muted:#8a8a8a;
  --line:#dcdcdc;
  --page:#f8faf5;
  --btn-grey:#e2e2e2;
}
*{box-sizing:border-box;margin:0;padding:0}
html,body{width:1200px;height:2381px;overflow:hidden}
body{position:relative;background:var(--page);font-family:"Open Sans",Arial,sans-serif;color:var(--text);font-size:12px;line-height:1.45}
.abs{position:absolute}
h2,h3,.nav a,.hero-title,.btn-join{font-family:"Ubuntu","Open Sans",sans-serif}

/* hero */
.hero-photo{left:0;top:0;width:1200px;height:600px;background:linear-gradient(180deg,#3f5d2e 0%,#6f8f4a 30%,#8fb3a3 55%,#2f6a5a 75%,#2c3b22 100%)}
.hero-edge{left:0;top:596px;width:1200px;height:8px;background:var(--page)}
.logo-badge{left:133px;top:26px;width:168px;height:168px;border-radius:50%;background:#fff;border:6px solid var(--green);display:flex;align-items:center;justify-content:center;text-align:center;font-family:"Ubuntu",sans-serif;font-weight:700;color:var(--green);font-size:24px;line-height:1.1}
.social{left:760px;top:62px;color:#fff;font-size:11px}
.social .icons{display:flex;gap:4px;margin-top:4px}
.social .icons span{width:20px;height:20px;background:#fff;border-radius:3px;opacity:.9}
.utility{left:900px;top:60px;color:#fff;font-size:11px}
.search{left:900px;top:82px;width:162px;height:24px;background:#fff;border-radius:2px;font-size:11px;color:#999;padding:4px 8px}
.nav{left:305px;top:132px;width:767px;height:40px;background:#fff;display:flex;align-items:stretch;box-shadow:0 1px 3px rgba(0,0,0,.2)}
.nav a{display:flex;align-items:center;padding:0 10px;font-size:14px;font-weight:700;color:#3a3a3a;text-decoration:none;text-transform:uppercase;border-right:1px solid #e4e4e4}
.nav a.active{background:var(--green);color:#fff}
.hero-title{left:140px;top:228px;color:#fff;font-size:62px;font-weight:700;line-height:68px;text-shadow:0 2px 6px rgba(0,0,0,.35)}
.btn-join{left:146px;top:449px;width:310px;height:52px;background:var(--brown);border-radius:4px;color:#fff;font-size:23px;font-weight:500;display:flex;align-items:center;justify-content:center;gap:10px}
.circle-arrow{width:22px;height:22px;border-radius:50%;background:#fff;display:inline-flex;align-items:center;justify-content:center}
.slide-arrow{top:345px;width:36px;height:36px;border-radius:50%;background:rgba(255,255,255,.35);display:flex;align-items:center;justify-content:center}
.video{left:566px;top:214px;width:507px;height:343px;background:#222;box-shadow:0 3px 10px rgba(0,0,0,.4)}
.video-screen{position:absolute;left:0;top:0;width:507px;height:310px;background:radial-gradient(circle at 50% 45%,#f2f2ee 0%,#c8ccc6 70%,#a9aea6 100%)}
.video-bar{position:absolute;left:0;top:310px;width:507px;height:33px;background:linear-gradient(#3a3a3a,#111);color:#ddd;font-size:11px;display:flex;align-items:center;gap:14px;padding:0 14px}
.video-progress{position:absolute;left:0;top:306px;width:507px;height:5px;background:#555}
.video-progress i{display:block;width:140px;height:5px;background:#c4161c}

/* section headings */
.sec-head{display:flex;align-items:center;gap:12px;border-bottom:1px solid var(--line);padding-bottom:8px}
.sec-head h2{font-size:21px;font-weight:700;color:var(--green-head)}
.tag{background:var(--lime);color:#fff;font-size:12px;font-weight:700;padding:1px 8px;border-radius:2px;font-family:"Open Sans",sans-serif}
.side-head{border-bottom:1px solid var(--line);padding-bottom:8px}
.side-head h2{font-size:21px;font-weight:500;color:var(--brown-dark)}
p.body{font-size:11.5px;line-height:17px}

.tiles{left:128px;top:788px;display:flex;gap:5px}
.tile{width:151px;height:134px;border:1px solid #d8e6d5;background:#fff;border-radius:4px;display:flex;flex-direction:column;align-items:center;justify-content:center;gap:12px;font-size:13px;font-weight:600;color:#333;text-align:center}
.tile.active{background:#7dbb87;color:#fff;border-color:#7dbb87;height:152px;clip-path:polygon(0 0,100% 0,100% 88%,50% 100%,0 88%)}
.bullets{left:128px;top:960px;width:616px}
.bullets li{list-style:none;display:flex;gap:16px;font-size:11.5px;line-height:17px;margin-bottom:20px}
.bullets li svg{flex:none;margin-top:2px}

.grid-btns{left:128px;top:1268px;display:grid;grid-template-columns:302px 302px;column-gap:12px;row-gap:7px}
.gbtn{height:38px;background:var(--btn-grey);border-radius:3px;display:flex;align-items:center;justify-content:space-between;padding:0 12px 0 16px;font-size:13px;font-weight:700;color:#555}
.gbtn.active{background:var(--brown);color:#fff}
.gbtn .dot{width:20px;height:20px;border-radius:50%;background:#bdbdbd;display:flex;align-items:center;justify-content:center}
.gbtn.active .dot{background:#fff}

.col-title{font-size:15px;font-weight:700;color:#222;display:flex;align-items:center;gap:10px}
.ticks li{list-style:none;display:flex;align-items:center;gap:10px;font-size:12px;height:26px}
.tick{width:11px;height:11px;border-radius:50%;background:var(--lime);flex:none}
.trip{display:flex;gap:8px;font-size:11.5px;line-height:15px;margin-bottom:13px}
.trip .thumb{width:24px;height:20px;flex:none;border-radius:2px}
.trip b{color:#222}
.brown-btn{height:33px;background:var(--brown);color:#fff;font-size:12.5px;display:flex;align-items:center;justify-content:center;border-radius:3px}

.partner-row{display:flex;gap:5px}
.partner-badge{width:120px;height:40px;border:1px solid #ddd;background:#f0f0f0}
.pager{display:flex;gap:4px}
.pager span{width:16px;height:16px;border-radius:50%;background:#888}
.pager span.on{background:var(--lime)}

/* right column */
.vline{left:789px;top:660px;width:1px;height:1370px;background:#e2e2e2}
.testi{display:flex;gap:14px;align-items:center}
.avatar{width:50px;height:48px;background:linear-gradient(#b8c7d6,#8797a6);border:2px solid #fff;box-shadow:0 0 2px rgba(0,0,0,.3)}
.testi b{display:block;font-size:15px;color:#222}
.testi span{font-size:12px;color:var(--green)}
.proposal{left:828px;top:1018px;width:244px;height:348px;background:linear-gradient(#2f8f2a,#2b7f26);padding:20px 14px}
.proposal h2{color:#fff;font-size:21px;font-weight:500;border-bottom:1px solid rgba(255,255,255,.35);padding-bottom:10px;margin-bottom:20px}
.field{background:#fff;height:25px;font-size:11px;color:#888;padding:4px 8px;margin-bottom:9px}
.field.area{height:111px}
.proposal .send{width:104px;height:32px;background:var(--brown);color:#fff;font-size:12px;display:flex;align-items:center;justify-content:center;border-radius:3px;margin-top:5px}
.tips li{list-style:none;display:flex;gap:10px;font-size:11.5px;line-height:17px;padding:8px 0;border-bottom:1px solid #e6e6e6}
.tips .tick{margin-top:3px}
.sub{font-size:15px;font-weight:700;color:#444}

/* footer */
.footer{left:0;top:2060px;width:1200px;height:196px;background:linear-gradient(#2f9a2c,#3f8a22)}
.foot-links{left:128px;top:2104px;color:#fff;font-size:12px;line-height:17px}
.foot-h{color:#fff;font-family:"Ubuntu",sans-serif;font-size:18px;font-weight:500;border-bottom:1px solid rgba(255,255,255,.5);padding-bottom:6px}
.foot-logo{left:920px;top:2082px;width:104px;height:104px;border-radius:50%;background:#fff;border:5px solid var(--green);display:flex;align-items:center;justify-content:center;text-align:center;font-family:"Ubuntu",sans-serif;font-weight:700;color:var(--green);font-size:15px;line-height:1.1}
.bottom{font-size:10.5px;color:#666;line-height:17px}
</style>
</head>
<body>

<!-- HERO -->
<div class="abs hero-photo" role="img" aria-label="Large photograph of a jungle waterfall and green pool in Guatemala"></div>
<div class="abs hero-edge"></div>

<div class="abs logo-badge">Moraby<br>Pathways</div>

<div class="abs social">Social Sharing
  <div class="icons"><span></span><span></span><span></span><span></span><span></span></div>
</div>
<div class="abs utility">Login &nbsp;|&nbsp; Register &nbsp;|&nbsp; Site Map</div>
<div class="abs search">Search</div>

<nav class="abs nav">
  <a href="#">Mission</a><a href="#">Programs</a><a href="#" class="active">Social Enterprise</a><a href="#">Products</a><a href="#">Travel &amp; Culture</a><a href="#">Speaking Circuits</a><a href="#" style="border-right:0">Contact</a>
</nav>

<div class="abs hero-title">Wander<br>Gather<br>Reach higher</div>
<div class="abs btn-join">Come along the Journey
  <span class="circle-arrow"><svg width="10" height="10" viewBox="0 0 10 10"><path d="M3 1l5 4-5 4z" fill="#4a2716"/></svg></span>
</div>

<div class="abs slide-arrow" style="left:73px"><svg width="14" height="14" viewBox="0 0 14 14"><path d="M9 2L4 7l5 5" stroke="#fff" stroke-width="2.5" fill="none"/></svg></div>
<div class="abs slide-arrow" style="left:1096px"><svg width="14" height="14" viewBox="0 0 14 14"><path d="M5 2l5 5-5 5" stroke="#fff" stroke-width="2.5" fill="none"/></svg></div>

<div class="abs video">
  <div class="video-screen" role="img" aria-label="Video still: Moraby Pathways title card for Harvest Nine Coffee with a leafy tree illustration"></div>
  <div class="video-progress"><i></i></div>
  <div class="video-bar">
    <svg width="12" height="12" viewBox="0 0 12 12"><rect x="2" y="1" width="3" height="10" fill="#ddd"/><rect x="7" y="1" width="3" height="10" fill="#ddd"/></svg>
    <svg width="14" height="12" viewBox="0 0 14 12"><path d="M1 4h3l4-3v10L4 8H1z" fill="#ddd"/></svg>
    <span>0:02 / 0:10</span>
    <span style="margin-left:auto">720p</span>
    <svg width="12" height="12" viewBox="0 0 12 12"><path d="M1 4V1h3M8 1h3v3M11 8v3H8M4 11H1V8" stroke="#ddd" fill="none" stroke-width="1.5"/></svg>
  </div>
</div>

<!-- ABOUT -->
<div class="abs sec-head" style="left:128px;top:678px;width:616px"><h2>About Moraby</h2><span class="tag">Wander</span></div>
<p class="abs body" style="left:128px;top:734px;width:616px">Lorem ipsum dolor sit amet, consectetuer adipiscing elit. Aenean commodo ligula eget dolor. Aenean massa. Cum sociis natoque penatibus et magnis dis parturient montes, nascetur ridiculus mus.</p>

<div class="abs tiles">
  <div class="tile active">
    <svg width="34" height="30" viewBox="0 0 34 30"><path d="M2 13L32 2 24 28 16 18z" fill="#fff"/></svg>
    Our Mission and<br>Philosophy
  </div>
  <div class="tile">
    <svg width="32" height="32" viewBox="0 0 32 32"><rect x="3" y="5" width="24" height="24" rx="3" fill="none" stroke="#7dbb87" stroke-width="3"/><path d="M12 21l2-6 12-12 4 4-12 12z" fill="#7dbb87"/></svg>
    History
  </div>
  <div class="tile">
    <svg width="50" height="34" viewBox="0 0 50 34"><circle cx="18" cy="9" r="8" fill="#7dbb87"/><circle cx="34" cy="11" r="7" fill="#7dbb87"/><path d="M2 34c0-12 8-16 16-16s16 4 16 16z" fill="#7dbb87"/><path d="M30 20c8 0 16 3 16 14H34z" fill="#7dbb87"/></svg>
    Advisory Board
  </div>
  <div class="tile">
    <svg width="52" height="32" viewBox="0 0 52 32"><ellipse cx="26" cy="18" rx="24" ry="12" fill="#7dbb87"/><circle cx="22" cy="10" r="10" fill="#7dbb87"/><circle cx="34" cy="12" r="8" fill="#7dbb87"/></svg>
    From the Founder
  </div>
</div>

<ul class="abs bullets">
  <li><svg width="16" height="16" viewBox="0 0 16 16"><circle cx="8" cy="8" r="3" fill="#3a8a2b"/><g fill="#3a8a2b"><circle cx="8" cy="2" r="2"/><circle cx="8" cy="14" r="2"/><circle cx="2" cy="8" r="2"/><circle cx="14" cy="8" r="2"/></g></svg>Because we believe that the best way to unlock your unique gifts and potential is by helping others unlock theirs.</li>
  <li><svg width="16" height="16" viewBox="0 0 16 16"><circle cx="8" cy="8" r="3" fill="#3a8a2b"/><g fill="#3a8a2b"><circle cx="8" cy="2" r="2"/><circle cx="8" cy="14" r="2"/><circle cx="2" cy="8" r="2"/><circle cx="14" cy="8" r="2"/></g></svg>Moraby Pathways is a social enterprise that utilizes social entrepreneurship principles and systems in order to "unlock" people's human potential in ways that support themselves, their families, and initiates positive social change.</li>
  <li><svg width="16" height="16" viewBox="0 0 16 16"><circle cx="8" cy="8" r="3" fill="#3a8a2b"/><g fill="#3a8a2b"><circle cx="8" cy="2" r="2"/><circle cx="8" cy="14" r="2"/><circle cx="2" cy="8" r="2"/><circle cx="14" cy="8" r="2"/></g></svg>Moraby Pathways organizes and leads expeditions to Guatemala in order to unlock human potential for both participant and recipient.</li>
</ul>

<!-- PROGRAMS -->
<div class="abs sec-head" style="left:128px;top:1158px;width:616px"><h2>Programs / Pricing</h2><span class="tag">Gather</span></div>
<p class="abs body" style="left:128px;top:1214px;width:616px">Lorem ipsum dolor sit amet, consectetuer adipiscing elit. Aenean commodo ligula eget dolor. Aenean massa. Cum sociis natoque penatibus et magnis dis parturient montes, nascetur ridiculus mus.</p>

<div class="abs grid-btns">
  <div class="gbtn active">Our Approach<span class="dot"><svg width="8" height="8" viewBox="0 0 8 8"><path d="M2 0l5 4-5 4z" fill="#4a2716"/></svg></span></div>
  <div class="gbtn">Our Partners here and Abroad<span class="dot"><svg width="8" height="8" viewBox="0 0 8 8"><path d="M2 0l5 4-5 4z" fill="#fff"/></svg></span></div>
  <div class="gbtn">Themed Trips<span class="dot"><svg width="8" height="8" viewBox="0 0 8 8"><path d="M2 0l5 4-5 4z" fill="#fff"/></svg></span></div>
  <div class="gbtn">Pricing and Sample Trips<span class="dot"><svg width="8" height="8" viewBox="0 0 8 8"><path d="M2 0l5 4-5 4z" fill="#fff"/></svg></span></div>
  <div class="gbtn">Past Trips Summaries<span class="dot"><svg width="8" height="8" viewBox="0 0 8 8"><path d="M2 0l5 4-5 4z" fill="#fff"/></svg></span></div>
  <div class="gbtn">The $5 Quest<span class="dot"><svg width="8" height="8" viewBox="0 0 8 8"><path d="M2 0l5 4-5 4z" fill="#fff"/></svg></span></div>
</div>

<!-- BENEFITS -->
<div class="abs sec-head" style="left:128px;top:1450px;width:616px;border-bottom:0"><h2>Benefits</h2><span class="tag">Reach higher</span></div>

<div class="abs" style="left:128px;top:1516px;width:290px">
  <div class="col-title"><svg width="22" height="20" viewBox="0 0 22 20"><path d="M1 2h4l3 11h11l2-8H7" stroke="#333" stroke-width="2" fill="none"/><circle cx="9" cy="17" r="2" fill="#333"/><circle cx="17" cy="17" r="2" fill="#333"/></svg>Online Store</div>
  <ul class="ticks" style="margin-top:14px">
    <li><span class="tick"></span>Aenean commodo ligula Lorem ipsum</li>
    <li><span class="tick"></span>Cum sociis natoque penatibus et magnis</li>
    <li><span class="tick"></span>Lorem ipsum dolor sit amet, consectetuer</li>
    <li><span class="tick"></span>Cum sociis natoque penatibus</li>
    <li><span class="tick"></span>Lorem ipsum dolor sit amet, consectetuer</li>
    <li><span class="tick"></span>Cum sociis natoque penatibus</li>
  </ul>
</div>
<div class="abs" style="left:419px;top:1516px;width:1px;height:210px;background:var(--line)"></div>

<div class="abs" style="left:468px;top:1516px;width:276px">
  <div class="col-title"><svg width="22" height="18" viewBox="0 0 22 18"><rect x="1" y="4" width="20" height="13" rx="2" fill="#333"/><rect x="7" y="1" width="8" height="4" fill="#333"/><circle cx="11" cy="10.5" r="4" fill="#fff"/><circle cx="11" cy="10.5" r="2" fill="#333"/></svg>Past Trips</div>
  <div style="margin-top:14px">
    <div class="trip"><div class="thumb" style="background:linear-gradient(#c9a27c,#7b5a3d)" role="img" aria-label="Trip thumbnail photo"></div><div><b>Aenean commodo</b> ligula Lorem ipsum dolor - <b>More</b> | 13 June 2012</div></div>
    <div class="trip"><div class="thumb" style="background:linear-gradient(#6f8fc0,#c0503a)" role="img" aria-label="Trip thumbnail photo"></div><div><b>Cum sociis natoque</b> penatibus et magnis dis parturient montes - <b>More</b> | 13 June 2012</div></div>
    <div class="trip"><div class="thumb" style="background:linear-gradient(#d9a77a,#8b5433)" role="img" aria-label="Trip thumbnail photo"></div><div><b>Lorem ipsum</b> dolor sit amet, consectetuer adipiscing elit. - <b>More</b> | 13 June 2012</div></div>
  </div>
</div>
<div class="abs brown-btn" style="left:468px;top:1690px;width:129px">Contact Our Team</div>
<div class="abs brown-btn" style="left:603px;top:1690px;width:141px">Request a Proposal</div>

<!-- PARTNERS -->
<div class="abs sec-head" style="left:128px;top:1772px;width:616px"><h2>Partners</h2></div>
<div class="abs" style="left:128px;top:1836px;width:616px;display:flex;justify-content:space-between;align-items:center">
  <span class="sub" style="color:#222">Partners in Guatemala</span><span class="pager"><span></span><span class="on"></span></span>
</div>
<div class="abs partner-row" style="left:128px;top:1868px">
  <div class="partner-badge"></div><div class="partner-badge"></div><div class="partner-badge"></div><div class="partner-badge"></div><div class="partner-badge"></div>
</div>
<div class="abs" style="left:128px;top:1946px;width:616px;display:flex;justify-content:space-between;align-items:center">
  <span class="sub" style="color:#222">Our Partners Abroad</span><span class="pager"><span></span><span class="on"></span></span>
</div>
<div class="abs partner-row" style="left:128px;top:1976px">
  <div class="partner-badge"></div><div class="partner-badge"></div><div class="partner-badge"></div><div class="partner-badge"></div><div class="partner-badge"></div>
</div>

<!-- RIGHT COLUMN -->
<div class="abs vline"></div>

<div class="abs side-head" style="left:828px;top:678px;width:244px"><h2>Moraby Testimonials</h2></div>
<div class="abs testi" style="left:828px;top:740px"><div class="avatar" role="img" aria-label="Portrait photo of Lena Hart"></div><div><b>Lena Hart</b><span>Advisor - Australia</span></div></div>
<p class="abs body" style="left:828px;top:798px;width:244px">Lorem ipsum dolor sit amet, consectetuer adipiscing elit. Aenean commodo ligula eget dolor. Aenean massa.</p>
<div class="abs testi" style="left:828px;top:869px"><div class="avatar" role="img" aria-label="Portrait photo of Owen Pike"></div><div><b>Owen Pike</b><span>Advisor - Australia</span></div></div>
<p class="abs body" style="left:828px;top:926px;width:244px">Cum sociis natoque penatibus et magnis dis parturient montes, nascetur ridiculus mus. Donec quam felis, ultricies nec</p>

<div class="abs proposal">
  <h2>Request a Proposal</h2>
  <div class="field">Your Name</div>
  <div class="field">Enter Email</div>
  <div class="field area">Message</div>
  <div class="send">Send Request</div>
</div>

<div class="abs side-head" style="left:828px;top:1406px;width:244px"><h2>Moraby Travel Tips</h2></div>
<ul class="abs tips" style="left:828px;top:1464px;width:244px">
  <li><span class="tick"></span>Cum sociis natoque penatibus et magnis</li>
  <li><span class="tick"></span>Cum sociis natoque penatibus et magnis dis parturient montes.</li>
  <li style="border-bottom:0"><span class="tick"></span>Cum sociis natoque penatibus et magnis</li>
</ul>

<div class="abs side-head" style="left:828px;top:1612px;width:244px"><h2>Moraby Business</h2></div>
<div class="abs sub" style="left:828px;top:1670px">Business Card</div>
<div class="abs" style="left:828px;top:1703px;font-size:10.5px">Front Side</div>
<div class="abs" style="left:977px;top:1703px;font-size:10.5px">Back Side</div>
<div class="abs" style="left:828px;top:1723px;width:115px;height:80px;background:#fff;border:1px solid #bfd9b8" role="img" aria-label="Front of the business card with logo and address"></div>
<div class="abs" style="left:977px;top:1723px;width:95px;height:163px;background:linear-gradient(#fff 0%,#eef6ea 60%,#5a3a26 100%);border:1px solid #bfd9b8" role="img" aria-label="Back of the business card with logo and founder details"></div>
<div class="abs sub" style="left:828px;top:1888px">Our Pamphlet</div>
<div class="abs" style="left:828px;top:1915px;width:115px;height:101px;background:linear-gradient(#8a6a52,#3e2e24)" role="img" aria-label="Pamphlet photo of a child in Guatemala"></div>
<div class="abs" style="left:943px;top:1915px;width:129px;height:101px;background:linear-gradient(135deg,#5f8a2f,#9a2f1e)" role="img" aria-label="Pamphlet photo of red and green coffee cherries"></div>

<!-- FOOTER -->
<div class="abs footer"></div>
<div class="abs foot-links">Mission<br>Programs<br>Social Enterprise<br>Products<br>Travel &amp; Culture<br>Speaking Circuits<br>Contact</div>
<div class="abs" style="left:312px;top:2100px;width:190px">
  <div class="foot-h">Newsletter Signup</div>
  <div style="margin-top:12px;background:#fff;height:26px;font-size:11px;color:#888;padding:5px 8px">Enter Email</div>
  <div style="margin-top:10px;width:82px;height:32px;background:var(--brown);color:#fff;font-size:12px;display:flex;align-items:center;justify-content:center;border-radius:3px">Subscribe</div>
</div>
<div class="abs" style="left:578px;top:2100px;width:270px">
  <div class="foot-h">Guatemala Profile</div>
  <p style="margin-top:12px;color:#fff;font-size:12px;line-height:17px">Lorem ipsum dolor sit amet, consectetuer adipiscing elit. Aenean commodo ligula eget dolor. Aenean massa. Cum sociis natoque</p>
</div>
<div class="abs foot-logo">Moraby<br>Pathways</div>

<div class="abs bottom" style="left:128px;top:2268px">All Right Reserve Copyright © 2012<br>With Moraby Pathways</div>
<div class="abs bottom" style="left:928px;top:2268px;text-align:right;width:144px">Privacy Policy &nbsp;|&nbsp; Terms of Use<br>Powered By : Loomwork Studio</div>

</body>
</html>
```